KerrLow Farm

Need a nice simple clean double sided business card that has our logo and info on:
Kerr Low Farm
Martin & Felicity Kerr Low
kerrlowfarm@mailbarn.example
Martin: 1-780-555-0148
Felicity: 1-780-555-0193
Instagram @ kerrlow_farm

Contact Information for Business Card

Martin & Felicity Kerr Low kerrlowfarm@mailbarn.example Martin: 1-780-555-0148 Felicity: 1-780-555-0193

```html
<!DOCTYPE html>
<html lang="en">
<head>
<meta charset="utf-8">
<title>Kerr Low Farm – Business Card</title>
<link href="https://fonts.googleapis.com/css2?family=Montserrat:wght@500;700&display=swap" rel="stylesheet">
<style>
  :root {
    --bg: #e4e4e4;
    --farm-green: #6aa142;
    --name-green: #3f9a45;
    --harvest-orange: #f5a01f;
    --white: #ffffff;
  }
  * { margin: 0; padding: 0; box-sizing: border-box; }
  html, body {
    width: 1200px; height: 1200px; overflow: hidden;
    background: var(--bg);
    font-family: "Montserrat", Arial, sans-serif;
  }
  .canvas { position: relative; width: 1200px; height: 1200px; }
  .card {
    position: absolute; left: 225px; width: 750px; height: 432px; overflow: hidden;
  }
  /* Front */
  .card-front { top: 113px; background: var(--farm-green); }
  .front-mark {
    position: absolute; left: 300px; top: 106px; width: 146px; height: 146px;
    border: 3px solid var(--white); border-radius: 50%;
  }
  .front-name {
    position: absolute; left: 0; right: 0; top: 262px; text-align: center;
    color: var(--white); font-weight: 700; font-size: 38px; letter-spacing: 1px;
  }
  /* Back */
  .card-back { top: 583px; background: var(--white); }
  .back-waves { position: absolute; inset: 0; width: 750px; height: 432px; }
  .edge-dot {
    position: absolute; left: -15px; top: 87px; width: 30px; height: 30px;
    border-radius: 50%; background: var(--name-green);
  }
  .owners {
    position: absolute; left: 26px; top: 86px;
    font-weight: 700; font-size: 25px; color: var(--name-green); letter-spacing: -0.2px;
  }
  .owners .amp { color: var(--harvest-orange); }
  .back-mark {
    position: absolute; left: 529px; top: 48px; width: 108px; height: 108px;
    border: 3px solid var(--farm-green); border-radius: 50%;
  }
  .back-name {
    position: absolute; left: 440px; width: 286px; top: 168px; text-align: center;
    color: var(--farm-green); font-weight: 700; font-size: 27px;
  }
  .contact-block { position: absolute; left: 34px; top: 256px; color: var(--white); }
  .contact-title { font-weight: 700; font-size: 24px; }
  .contact-rule { width: 30px; height: 3px; background: var(--white); margin: 14px 0 12px; }
  .contact-list { list-style: none; }
  .contact-list li {
    display: flex; align-items: center; gap: 12px;
    font-weight: 500; font-size: 18px; height: 30px;
  }
  .contact-list svg { width: 18px; height: 18px; flex: none; }
</style>
</head>
<body>
<div class="canvas">

  <section class="card card-front">
    <div class="front-mark"></div>
    <div class="front-name">KERR LOW FARM</div>
  </section>

  <section class="card card-back">
    <svg class="back-waves" viewBox="0 0 750 432" aria-hidden="true">
      <path d="M0,192 C90,170 210,172 356,228 C230,196 110,192 0,214 Z" fill="var(--farm-green)"/>
      <path d="M10,226 C150,195 280,205 420,262 C540,315 640,345 750,308 L750,330 C640,365 530,330 410,276 C290,222 160,210 10,226 Z" fill="var(--harvest-orange)"/>
      <path d="M0,238 C150,205 290,220 410,284 C530,347 640,370 750,340 L750,432 L0,432 Z" fill="var(--farm-green)"/>
    </svg>

    <div class="edge-dot"></div>
    <div class="owners">MARTIN <span class="amp">&amp;</span> FELICITY KERR LOW</div>

    <div class="back-mark"></div>
    <div class="back-name">KERR LOW FARM</div>

    <div class="contact-block">
      <div class="contact-title">KERR LOW FARM</div>
      <div class="contact-rule"></div>
      <ul class="contact-list">
        <li>
          <svg viewBox="0 0 24 24" aria-hidden="true"><path fill="#fff" d="M6.6 10.8a15 15 0 0 0 6.6 6.6l2.2-2.2a1 1 0 0 1 1-.25 11 11 0 0 0 3.6.6 1 1 0 0 1 1 1V20a1 1 0 0 1-1 1A17 17 0 0 1 3 4a1 1 0 0 1 1-1h3.5a1 1 0 0 1 1 1 11 11 0 0 0 .6 3.6 1 1 0 0 1-.25 1z"/></svg>
          kerrlowfarm@mailbarn.example
        </li>
        <li>
          <svg viewBox="0 0 24 24" aria-hidden="true"><path fill="#fff" d="M2 5h20v14H2z"/><path d="M2 5l10 8 10-8" fill="none" stroke="#6aa142" stroke-width="2"/></svg>
          Martin: 1-780-555-0148
        </li>
        <li>
          <svg viewBox="0 0 24 24" aria-hidden="true"><circle cx="12" cy="12" r="10" fill="#fff"/><path d="M2 12h20M12 2c3 3 3 17 0 20M12 2c-3 3-3 17 0 20" fill="none" stroke="#6aa142" stroke-width="1.5"/></svg>
          Felicity: 1-780-555-0193
        </li>
      </ul>
    </div>
  </section>

</div>
</body>
</html>
```